Lift-Lark needs a design for a new mobile app

A new app - lift-lark.example, requires a design for its new app.

The app lets users add, create and share gym sessions. Sessions can be created, sets added and exercises chosen.

The app is currently functional on Android only (ios later), all that is required is a design for the app.

Some design assets are available (logo, colours, font), so the app should tie into these.

The design needs to be clean, simple and obvious, and all design assets will be required as part of this project.

One of the pages has % complete on the set - an icon to demonstrate this rather than a text based (eg 50%) would be great.

Screenshots will be available, along with the logos, colours and fonts.

Target Market(s)

Gym goers, all ages, male & female, fitness enthusiasts
Users of phones and tablets

Industry/Entity Type

Gym

Requirements
Must have
• Designs examples for each of the screens in the app, and an obvious selection of reusable elements (such as drop downs, radio buttons, buttons, calendar selectors, check boxes etc)
• Colours, logos and branding to fit into what is already available on the website.
• Usability and consistency are vital. Buttons should be in the same place (where possible).
• Design should help the user to complete the journey, and not get in the way.
• It should be a pleasure to use the app.
• Happy to have white space where appropriate.
• We use native elements where available.
Should not have
• Design features that waste space

```html
<!DOCTYPE html>
<html lang="en">
<head>
<meta charset="utf-8">
<title>Lift-Lark · Add/Edit weight and reps</title>
<link rel="stylesheet" href="https://fonts.googleapis.com/css2?family=Montserrat:wght@400;500&family=Roboto:wght@400&display=swap">
<style>
:root{
  --page:#ffffff;
  --status:#0b2a3b;
  --toolbar:#0f3550;
  --toolbar-ink:#6e8798;
  --tabs:#3f3f3f;
  --tab-ink:#6a6a6a;
  --tab-active:#2f6d96;
  --scrim:#4f4f4f;
  --dialog:#ffffff;
  --ink:#454545;
  --muted:#8a8a8a;
  --faint:#b8b8b8;
  --field:#f0f0f0;
  --accent:#2a8fd0;
  --kb:#eceff1;
  --kb-strip:#e4e8ea;
  --key-ink:#37474f;
  --kb-teal:#4db6ac;
  --space:#cfd4d7;
}
*{box-sizing:border-box;margin:0;padding:0}
html,body{width:1059px;height:1200px;overflow:hidden;background:var(--page)}
.screen{position:absolute;left:212px;top:35px;width:635px;height:1129px;overflow:hidden;font-family:"Montserrat",sans-serif;background:var(--scrim)}
.status-bar{position:absolute;left:0;top:0;width:100%;height:42px;background:var(--status)}
.status-bar svg{position:absolute;left:450px;top:8px}
.status-time{position:absolute;right:12px;top:6px;font:500 24px "Roboto",sans-serif;color:#5b6f7b}
.toolbar{position:absolute;left:0;top:42px;width:100%;height:88px;background:var(--toolbar)}
.toolbar-title{position:absolute;left:89px;top:28px;font-size:21px;font-weight:500;color:var(--toolbar-ink)}
.toolbar svg{position:absolute}
.tabs{position:absolute;left:0;top:130px;width:100%;height:53px;background:var(--tabs);display:flex}
.tab{flex:1;text-align:center;line-height:53px;font-size:19px;font-weight:500;color:var(--tab-ink);border-right:1px solid #464646}
.tab.is-active{color:var(--tab-active);border-bottom:3px solid var(--tab-active);line-height:50px}
.dialog{position:absolute;left:44px;top:280px;width:547px;height:340px;background:var(--dialog)}
.dialog-title{position:absolute;top:22px;width:100%;text-align:center;font-size:21px;font-weight:500;color:var(--ink)}
.field-label{position:absolute;top:81px;font-size:17px;color:var(--ink)}
.weight-input{position:absolute;left:37px;top:113px;width:200px;height:43px;background:var(--field)}
.weight-input::before{content:"";position:absolute;left:11px;top:9px;width:1.5px;height:25px;background:var(--accent)}
.divider{position:absolute;left:273px;top:85px;width:1px;height:200px;background:#e3e3e3}
.picker-item{position:absolute;left:309px;width:199px;text-align:center;color:var(--muted)}
.picker-item.is-selected{top:167px;height:42px;line-height:42px;background:var(--field);color:var(--accent);font-size:17px}
.dialog-action{position:absolute;top:298px;font-size:19px;transform:translateX(-50%)}
.dialog-action.cancel{left:136px;color:var(--muted)}
.dialog-action.confirm{left:410px;color:var(--accent)}
.keyboard{position:absolute;left:0;top:759px;width:100%;height:370px;background:var(--kb);font-family:"Roboto",sans-serif;color:var(--key-ink)}
.suggestions{position:absolute;top:0;width:100%;height:47px;background:var(--kb-strip)}
.suggestions i{position:absolute;top:12px;width:1px;height:24px;background:#c5cacd}
.key{position:absolute;width:50px;text-align:center;font-size:30px;transform:translate(-50%,-50%)}
.key sup{position:absolute;left:12px;top:-20px;font-size:13px}
.key.small{font-size:19px}
.spacebar{position:absolute;left:124px;top:313px;width:394px;height:24px;border-radius:3px;background:var(--space)}
.kb-icon{position:absolute}
</style>
</head>
<body>
<main class="screen">
  <header class="status-bar">
    <svg width="80" height="26" viewBox="0 0 80 26" aria-hidden="true">
      <path d="M0 4 Q17 -6 34 4 L17 24 Z" fill="#5b6f7b"/>
      <path d="M40 24 L62 2 L62 24 Z" fill="#5b6f7b"/>
    </svg>
    <svg class="battery" width="20" height="26" style="left:528px;top:8px" aria-hidden="true"><rect x="2" y="3" width="14" height="22" fill="#5b6f7b"/><rect x="6" y="0" width="6" height="4" fill="#5b6f7b"/></svg>
    <span class="status-time">12:30</span>
  </header>
  <nav class="toolbar">
    <svg width="32" height="24" style="left:14px;top:32px" aria-hidden="true"><path d="M30 12H3M13 2L3 12L13 22" fill="none" stroke="#6e8798" stroke-width="2.5"/></svg>
    <span class="toolbar-title">Bench Press</span>
    <svg width="26" height="26" style="left:517px;top:197px;top:30px" aria-hidden="true"><circle cx="13" cy="13" r="13" fill="#6e8798"/><rect x="11.5" y="10" width="3" height="10" fill="#0f3550"/><circle cx="13" cy="6.5" r="1.8" fill="#0f3550"/></svg>
    <svg width="24" height="26" style="left:598px;top:29px" aria-hidden="true"><rect x="1" y="4" width="22" height="20" fill="none" stroke="#6e8798" stroke-width="2"/><rect x="1" y="4" width="22" height="5" fill="#6e8798"/><path d="M6 1v5M18 1v5" stroke="#6e8798" stroke-width="2"/><path d="M5 13h3M10.5 13h3M16 13h3M5 18h3M10.5 18h3M16 18h3" stroke="#6e8798" stroke-width="2.5"/></svg>
  </nav>
  <div class="tabs">
    <div class="tab is-active">Sets</div>
    <div class="tab">History</div>
    <div class="tab" style="border-right:0">Records</div>
  </div>
  <section class="dialog">
    <h2 class="dialog-title">Add/Edit weight and reps</h2>
    <span class="field-label" style="left:37px">Weight</span>
    <div class="weight-input"></div>
    <div class="divider"></div>
    <span class="field-label" style="left:307px">Reps</span>
    <span class="picker-item" style="top:111px;font-size:12px;color:var(--faint)">99</span>
    <span class="picker-item" style="top:145px;font-size:14px">100</span>
    <span class="picker-item is-selected">0</span>
    <span class="picker-item" style="top:215px;font-size:14px">1</span>
    <span class="picker-item" style="top:251px;font-size:12px;color:var(--faint)">2</span>
    <span class="dialog-action cancel">Cancel</span>
    <span class="dialog-action confirm">OK, Save it</span>
  </section>
  <div class="keyboard">
    <div class="suggestions"><i style="left:222px"></i><i style="left:412px"></i>
      <svg class="kb-icon" width="14" height="22" style="left:602px;top:13px" aria-hidden="true"><rect x="4" y="0" width="6" height="13" rx="3" fill="#546e7a"/><path d="M1 9a6 6 0 0 0 12 0M7 15v6" fill="none" stroke="#546e7a" stroke-width="1.8"/></svg>
    </div>
    <span class="key" style="left:26px;top:88px"><sup>1</sup>Q</span>
    <span class="key" style="left:84px;top:88px"><sup>2</sup>W</span>
    <span class="key" style="left:141px;top:88px"><sup>3</sup>E</span>
    <span class="key" style="left:199px;top:88px"><sup>4</sup>R</span>
    <span class="key" style="left:256px;top:88px"><sup>5</sup>T</span>
    <span class="key" style="left:314px;top:88px"><sup>6</sup>Y</span>
    <span class="key" style="left:372px;top:88px"><sup>7</sup>U</span>
    <span class="key" style="left:430px;top:88px"><sup>8</sup>I</span>
    <span class="key" style="left:487px;top:88px"><sup>9</sup>O</span>
    <span class="key" style="left:545px;top:88px"><sup>0</sup>P</span>
    <svg class="kb-icon" width="28" height="20" style="left:592px;top:244px;top:244px;top:244px;top:244px;top:244px;top:244px;top:244px;top:244px;top:244px;top:244px;top:244px;top:244px;top:244px;top:244px;top:244px;top:244px;top:244px;top:244px;top:244px;top:244px;top:244px;top:244px;top:244px;top:244px;top:244px;top:244px;top:244px;top:244px;top:244px;top:244px;top:244px;top:244px;top:244px;top:244px;top:244px;top:244px;top:244px;top:244px;top:244px;top:244px;top:244px;top:244px;top:244px;top:244px;top:244px;top:244px;top:244px;top:244px;top:244px;top:78px" aria-hidden="true"><path d="M8 1H27V19H8L1 10Z" fill="#78909c"/><path d="M13 6l8 8M21 6l-8 8" stroke="#eceff1" stroke-width="2"/></svg>
    <span class="key" style="left:55px;top:167px">A</span>
    <span class="key" style="left:113px;top:167px">S</span>
    <span class="key" style="left:170px;top:167px">D</span>
    <span class="key" style="left:228px;top:167px">F</span>
    <span class="key" style="left:286px;top:167px">G</span>
    <span class="key" style="left:343px;top:167px">H</span>
    <span class="key" style="left:401px;top:167px">J</span>
    <span class="key" style="left:459px;top:167px">K</span>
    <span class="key" style="left:516px;top:167px">L</span>
    <svg class="kb-icon" width="38" height="38" style="left:572px;top:148px" aria-hidden="true"><circle cx="19" cy="19" r="19" fill="#4db6ac"/><path d="M27 13v6H12M16 15l-4 4 4 4" fill="none" stroke="#fff" stroke-width="2.2"/></svg>
    <svg class="kb-icon" width="28" height="34" style="left:15px;top:232px" aria-hidden="true"><path d="M14 2L26 14H19V21H9V14H2Z" fill="#4db6ac"/><path d="M5 32h18" stroke="#78909c" stroke-width="2"/></svg>
    <span class="key" style="left:89px;top:246px">Z</span>
    <span class="key" style="left:147px;top:246px">X</span>
    <span class="key" style="left:205px;top:246px">C</span>
    <span class="key" style="left:263px;top:246px">V</span>
    <span class="key" style="left:321px;top:246px">B</span>
    <span class="key" style="left:378px;top:246px">N</span>
    <span class="key" style="left:436px;top:246px">M</span>
    <span class="key" style="left:494px;top:246px">!</span>
    <span class="key" style="left:551px;top:246px">?</span>
    <svg class="kb-icon" width="28" height="34" style="left:595px;top:232px" aria-hidden="true"><path d="M14 2L26 14H19V21H9V14H2Z" fill="#4db6ac"/><path d="M5 32h18" stroke="#78909c" stroke-width="2"/></svg>
    <span class="key small" style="left:29px;top:325px">?123</span>
    <span class="key" style="left:89px;top:325px">,</span>
    <div class="spacebar"></div>
    <span class="key" style="left:551px;top:322px">.</span>
    <svg class="kb-icon" width="24" height="24" style="left:597px;top:313px" aria-hidden="true"><circle cx="12" cy="12" r="10" fill="none" stroke="#37474f" stroke-width="2"/><circle cx="8.5" cy="9.5" r="1.5" fill="#37474f"/><circle cx="15.5" cy="9.5" r="1.5" fill="#37474f"/><path d="M7 14a5.5 5.5 0 0 0 10 0Z" fill="#37474f"/></svg>
  </div>
</main>
</body>
</html>
```